Poster for a online company that buys your stuff

SwapKestrel offers a website which customers can get a instant offer for stuff their looking to sell. They then Courier the items in to us and they get paid the same day it arrives
We're looking for an eye catching design which portrays our hassle free process
We'll need your help to come up with a slogan/catch phrase and our easy 1,2,3 process so customers can see the poster and instantly have a clear understanding of what we do
1. Get an instant offer on our website
2. Send your item(s) to us
3.Get paid within 24 Hours
Industry/Entity Type
It Company
Look and feel
Each slider illustrates characteristics of the customer's brand and the style your logo design should communicate.

```html
<!DOCTYPE html>
<html lang="en">
<head>
<meta charset="utf-8">
<title>SwapKestrel – Trading, simple as a, b, c</title>
<link rel="stylesheet" href="https://fonts.googleapis.com/css2?family=Jura:wght@300;400&family=Open+Sans:wght@400;700&display=swap">
<style>
  :root {
    --bg-green: #9bcb3d;
    --panel-green: #9ccd41;
    --panel-shadow: #5f7f22;
    --headline-grey: #e4e4e4;
    --accent-red: #f2333a;
    --accent-green: #2ebd18;
    --accent-blue: #1148c8;
    --bag-text: #ffffff;
    --brand-dark: #2f2f2a;
    --mascot-tone: #e8a12e;
  }
  * { margin: 0; padding: 0; box-sizing: border-box; }
  html, body { width: 1200px; height: 1000px; overflow: hidden; }
  body { background: var(--bg-green); font-family: "Open Sans", sans-serif; }
  .poster { position: relative; width: 1200px; height: 1000px; background: var(--bg-green); }

  .brand-panel { position: absolute; left: 370px; top: 12px; width: 545px; height: 350px; }

  .mascot {
    position: absolute; left: 535px; top: 30px; width: 225px; height: 225px;
    border-radius: 50%;
    background: radial-gradient(circle at 50% 45%, #f3c462 0%, var(--mascot-tone) 55%, #5b8a2a 100%);
    opacity: .85;
  }
  .brand-name {
    position: absolute; left: 505px; top: 252px; width: 265px; text-align: center;
    font-family: "Open Sans", sans-serif; font-weight: 700; font-size: 36px;
    color: var(--brand-dark); letter-spacing: -0.5px;
  }

  .headline {
    position: absolute; left: 76px; top: 470px; white-space: nowrap;
    font-family: "Jura", sans-serif; font-weight: 300; font-size: 86px;
    color: var(--headline-grey); letter-spacing: 1px;
  }
  .headline .gap { display: inline-block; width: 48px; }
  .headline .gap-lg { display: inline-block; width: 52px; }
  .letter-a { color: var(--accent-red); }
  .letter-b { color: var(--accent-green); }
  .letter-c { color: var(--accent-blue); }

  .step { position: absolute; }
  .step svg { position: absolute; left: 0; top: 0; }
  .step-label {
    position: absolute; font-size: 36px; color: var(--bag-text); font-weight: 400;
  }
  .step-text {
    position: absolute; font-size: 31px; line-height: 40px; color: var(--bag-text);
    font-weight: 400; letter-spacing: 0.5px;
  }
  .step-a { left: 78px; top: 595px; width: 330px; height: 315px; }
  .step-b { left: 443px; top: 578px; width: 335px; height: 315px; }
  .step-c { left: 810px; top: 578px; width: 335px; height: 295px; }
</style>
</head>
<body>
<main class="poster">

  <svg class="brand-panel" viewBox="0 0 545 350" width="545" height="350" aria-hidden="true">
    <polygon points="12,10 408,6 538,172 408,340 12,338" fill="var(--panel-shadow)" opacity=".7"/>
    <polygon points="8,6 404,4 532,170 402,334 8,332" fill="var(--panel-green)"/>
  </svg>
  <div class="mascot" role="img" aria-label="Cartoon courier mascot giving a thumbs up while carrying a parcel"></div>
  <div class="brand-name">SwapKestrel</div>

  <h1 class="headline">Trading,simple<span class="gap"></span>as<span class="gap-lg"></span><span class="letter-a">a</span>,<span class="letter-b">b</span>,<span class="letter-c">c</span>.</h1>

  <section class="step step-a">
    <svg width="330" height="315" viewBox="0 0 330 315" role="img" aria-label="Red shopping bag">
      <defs>
        <linearGradient id="bagRed" x1="0" y1="0" x2="1" y2="1">
          <stop offset="0" stop-color="#ff3b3b"/><stop offset=".6" stop-color="#e81f26"/><stop offset="1" stop-color="#a50d12"/>
        </linearGradient>
      </defs>
      <polygon points="2,60 325,38 318,305 6,315" fill="url(#bagRed)"/>
    </svg>
    <div class="step-label" style="left:278px; top:52px;">a.</div>
    <div class="step-text" style="left:60px; top:92px;">Get an<br>instant<br>offer on<br>our website.</div>
  </section>

  <section class="step step-b">
    <svg width="335" height="315" viewBox="0 0 335 315" role="img" aria-label="Green shopping bag">
      <defs>
        <linearGradient id="bagGreen" x1="0" y1="0" x2="1" y2="1">
          <stop offset="0" stop-color="#3ed81f"/><stop offset=".6" stop-color="#22c40f"/><stop offset="1" stop-color="#138a07"/>
        </linearGradient>
      </defs>
      <polygon points="4,55 332,38 330,310 2,312" fill="url(#bagGreen)"/>
    </svg>
    <div class="step-label" style="left:285px; top:52px;">b.</div>
    <div class="step-text" style="left:70px; top:110px;">Send your<br>item(s)<br>to us.</div>
  </section>

  <section class="step step-c">
    <svg width="335" height="295" viewBox="0 0 335 295" role="img" aria-label="Blue shopping bag">
      <defs>
        <linearGradient id="bagBlue" x1="0" y1="0" x2="1" y2="1">
          <stop offset="0" stop-color="#1f6be8"/><stop offset=".6" stop-color="#0d4fd6"/><stop offset="1" stop-color="#06208a"/>
        </linearGradient>
      </defs>
      <polygon points="6,45 330,30 328,285 2,292" fill="url(#bagBlue)"/>
    </svg>
    <div class="step-label" style="left:285px; top:40px;">c.</div>
    <div class="step-text" style="left:90px; top:102px;">Get paid<br>within<br>24 hours.</div>
  </section>

</main>
</body>
</html>
```